Etiketten-Design für Mango-Chili Sauce
Zielgruppe
Saucen über den online-shop und in Supermärkten verkaufen. Das Etikett ist für eine Mango-Chilli Sauce.
Aufgabenstellung
Ich brauche ein Flaschenetikett sowie Firmenlogo
-Die Firma heisst The Drizzle
-Im Anhang zwei Fotos der Flasche. Fassvermögen ist 200ml.
-Beim Format des Etiketts bin ich offen für Vorschläge. Sollte mir das Design gefallen, möchte ich es auch skalieren können, damit es auf andere Flaschenformate passt.
Design: Ich möchte das das Etikett Qualität ausstrahlt und modern (schlicht) gestaltet ist. Zudem soll mich das Design zum Kauf antreiben.

```html
<!DOCTYPE html>
<html lang="de">
<head>
<meta charset="utf-8">
<title>The Drizzle – Chili Mango Etikett</title>
<link rel="stylesheet" href="https://fonts.googleapis.com/css2?family=Josefin+Sans:wght@300;700&display=swap">
<style>
  :root {
    --canvas: #ffffff;
    --ink: #111111;
    --paper: #f7f7f5;
    --paper-shade: #e6e6e2;
    --night: #1c1c1c;
    --night-shade: #2e2e2e;
    --night-edge: #121212;
    --light-text: #f2f2f2;
  }
  * { box-sizing: border-box; margin: 0; padding: 0; }
  html, body {
    width: 881px;
    height: 1200px;
    overflow: hidden;
    background: var(--canvas);
  }
  .canvas {
    width: 881px;
    height: 1200px;
    display: flex;
    justify-content: center;
    align-items: center;
    gap: 60px;
    font-family: "Josefin Sans", sans-serif;
  }
  .label {
    width: 380px;
    height: 560px;
    display: flex;
    flex-direction: column;
    align-items: center;
    padding-top: 72px;
  }
  .label--light {
    color: var(--ink);
    background: radial-gradient(ellipse at 40% 35%, var(--paper) 0%, var(--paper) 55%, var(--paper-shade) 100%);
    border: 6px solid var(--ink);
  }
  .label--dark {
    color: var(--light-text);
    background: radial-gradient(ellipse at 50% 40%, var(--night-shade) 0%, var(--night) 70%, var(--night-edge) 100%);
    padding-top: 78px;
  }
  .brand {
    font-weight: 700;
    font-size: 38px;
    letter-spacing: 1px;
    text-transform: uppercase;
    line-height: 1;
    white-space: nowrap;
  }
  .flavour {
    margin-top: 124px;
    font-weight: 300;
    font-size: 54px;
    line-height: 1.12;
    letter-spacing: 4px;
    text-align: center;
    text-transform: uppercase;
  }
  .divider {
    margin-top: 26px;
    display: flex;
    align-items: center;
    gap: 12px;
  }
  .divider__line {
    width: 48px;
    height: 2px;
    background: currentColor;
  }
  .divider__chili {
    width: 26px;
    height: 14px;
    border-radius: 3px;
    background: currentColor;
  }
</style>
</head>
<body>
  <main class="canvas">
    <section class="label label--light" aria-label="Etikett hell">
      <p class="brand">The Drizzle</p>
      <h1 class="flavour">Chili<br>Mango</h1>
      <div class="divider">
        <span class="divider__line"></span>
        <span class="divider__chili" role="img" aria-label="Kleine Chilischoten-Illustration"></span>
        <span class="divider__line"></span>
      </div>
    </section>

    <section class="label label--dark" aria-label="Etikett dunkel">
      <p class="brand">The Drizzle</p>
      <h2 class="flavour">Chili<br>Mango</h2>
      <div class="divider">
        <span class="divider__line"></span>
        <span class="divider__chili" role="img" aria-label="Kleine Chilischoten-Illustration"></span>
        <span class="divider__line"></span>
      </div>
    </section>
  </main>
</body>
</html>
```